Hair Extension Aftercare sheet

This sheet is to give to customers regarding the aftercare of hair extensions. There should be Simple and minimal look - approx A5 size and can be folded to suit. I have attached the content and logo files for use.
We are not looking for to much artwork just clean, professional look.
All the content provided in a compact flyer format i.e
A foldable A5 pamphlet or the like, this is for packaging requirements
Please do not submit A4 layouts

Industry/Entity Type

Hair And Beauty

Requirements
Must have
• All the content provided in a compact flyer format i.e
• A foldable A5 pamphlet or the like, this is for packaging requirements
Should not have
• tacky art work or images - must be clean lines

```html
<!DOCTYPE html>
<html lang="en">
<head>
<meta charset="utf-8">
<title>Hair Extension Aftercare and Maintenance Guidelines</title>
<link rel="stylesheet" href="https://fonts.googleapis.com/css2?family=Inter:wght@400;600;700&family=Montserrat:wght@600&display=swap">
<style>
  :root {
    --paper: #ffffff;
    --ink: #1d1d1b;
    --alert: #e2231a;
  }
  * { box-sizing: border-box; margin: 0; padding: 0; }
  html, body { width: 1200px; height: 848px; overflow: hidden; background: var(--paper); }
  .sheet {
    width: 1200px; height: 848px;
    display: grid;
    grid-template-columns: 358px 356px 358px;
    column-gap: 32px;
    padding: 28px 32px 0 32px;
    color: var(--ink);
    font-family: "Inter", Helvetica, Arial, sans-serif;
    font-size: 14.4px;
    line-height: 18.8px;
    overflow: hidden;
  }
  .panel { overflow: hidden; }
  .panel p { text-align: justify; margin-bottom: 8px; }
  .panel p.centered { text-align: center; }
  .sheet-title {
    font-family: "Montserrat", Helvetica, Arial, sans-serif;
    font-weight: 600;
    font-size: 17.5px;
    letter-spacing: 1.6px;
    line-height: 22px;
    text-align: center;
    text-transform: uppercase;
    margin: 2px 0 6px;
  }
  .section-title {
    font-weight: 700;
    font-size: 15px;
    text-align: center;
    text-transform: uppercase;
    margin: 10px 0 7px;
  }
  .panel > .section-title:first-child { margin-top: 0; }
  .alert-box {
    border: 1.5px solid var(--alert);
    color: var(--alert);
    font-weight: 600;
    font-size: 15px;
    line-height: 19px;
    text-align: center;
    padding: 6px 10px 7px;
    margin: 8px 0 12px;
  }
  .alert-box.major { margin-top: 6px; padding: 6px 8px 6px; }
  .alert-box .label { display: block; margin-bottom: 7px; }
  .panel p.lead-in { margin-bottom: 6px; }
  strong { font-weight: 700; }
</style>
</head>
<body>
<main class="sheet">
  <section class="panel">
    <h1 class="sheet-title">Aftercare and Maintenance Guidelines</h1>
    <p>It is very important to keep this exceptional quality hair in the best condition you can.&nbsp; Please read all of the information below:</p>
    <p>It is important to use the right tools for the job. A good hair brush is a small investment to keep your hair in the best possible condition and contributes to a pleasant wearing experience.</p>
    <p><strong>Mara Ellison Bristle Brushes</strong> with small plastic pins and real bristle hair are ideal and specially developed for this purpose. It smooths the hair without loosing brushing grip and removes tangles effortlessly.</p>
    <h2 class="section-title">General:</h2>
    <p>Do not use oil based products, always use water dissolvable products. Oil based products will keep the hair in a wet condition and can cause matting. Oil based products attract a lot more dust and dirt which will make the hair less smooth and feel dry.</p>
    <h2 class="section-title">General Washing &amp; Conditioning:</h2>
    <p>Shampoo at least two times per week. Never wash, brush or dry the hair upside down. Before washing, brush out all tangles with a hair extension brush (available from Mara Ellison Hair Extensions). Do not use a brush with only plastic or steel pins. Always start brushing or combing at the ends, working your way up to the roots.</p>
    <p>Wet the hair thoroughly, then dispense a small amount of shampoo into your hand and rub your hands together. Apply the shampoo evenly on the scalp and at the roots. Gently wash the scalp using your fingertips without rubbing the hair. Rinse thoroughly while squeezing the hair to remove all shampoo residue. If the shampoo does not foam the first time, don’t apply more shampoo but continue washing as normal. After rinsing simply re-apply the shampoo for a second time. There is no need</p>
  </section>

  <section class="panel">
    <p>to apply a lot of shampoo in the lengths. The hair will get cleaned when you rinse the hair out (unless extremely dirty).</p>
    <div class="alert-box">Avoid: Shampoos that contain sulphates &amp; products that are oil based.</div>
    <p class="centered">If you can’t wash it off your hands without shampoo, it is more likely oil based.</p>
    <h2 class="section-title">After you washed the hair:</h2>
    <p>After washing you may use a conditioner however, apply the conditioner from the ends to half way up the length. Never at the roots. Comb the conditioner through using a large wide tooth comb until all tangles are removed. Rinse thoroughly to leave no residue in the hair. Towel dry the hair by squeezing it with the towel. Don’t rub or massage the hair.</p>
    <p>You can apply small amounts of leave-in conditioner or a recommended styling product, comb through with your fingers into the direction you would like your hair to fall and scruntch it upwards once more. After you have done this leave the hair to dry completely without touching, combing or brushing it. = Best natural result.</p>
    <p>Let it dry naturally or use your favourite styling equipment. Use leave in conditioners only at the ends! When the hair is completely dry.</p>
    <h2 class="section-title">At Night</h2>
    <p>Braid the hair in a large loose braid at the nape of the neck before going to sleep. Do not sleep with wet hair, this will cause tangling and will make it difficult to style the following morning.</p>
    <h2 class="section-title">Styling the Hair</h2>
    <p>You can use a ceramic straightening iron or a hair dryer with a bristle brush to smooth the hair. Other styling tools that can be used are: Heated rollers, steam rollers, curling irons, hot air curling tongs and setting rollers.</p>
  </section>

  <section class="panel">
    <div class="alert-box major"><span class="label">IMPORTANT:</span>NEVER USE HOT STYLING EQUIPMENT THAT EXCEEDS 200 DEGREES CELSIUS OR 392 DEGREES FAHRENHEIT.</div>
    <p>Temperatures above this can damage the protein in the hair causing it to solidify and make the hair dry and unmanageable. Always keep hot styling equipment moving through the hair and do not hold for too long in one place. We do not recommend using straightening irons on wet hair.</p>
    <h2 class="section-title">Sports and Other Activities</h2>
    <p>Don’t expose your hair to strong windy conditions like sailing, motor sports, cabriolet cars. Wear protective head wear. If you sweat a lot during work outs, at least rinse out the saltiness as this will dry out the hair.</p>
    <h2 class="section-title">Visiting Saunas and Steam Rooms</h2>
    <p>Braid the hair in a loose braid in the nape of the neck and put it up using a hair clip. The hair can get very hot and can be painful when it touches the skin just like your own natural hair. Only brush the hair when it is cooled down. After the sauna rinse the hair under the shower and preferably wash the hair and condition it at the end of the visit or when you get home as stated in this aftercare sheet.</p>
    <h2 class="section-title">Swimming</h2>
    <p>It is not recommended that you swim while wearing curly, deep curly and deep curl textures, you can swim but don’t submerge your head in the water. If you swim every day or frequently, other textures are more suitable. Other textures before swimming, brush out any tangles. Make one braid at the nape of your neck. Try to keep your hair out of the water as much as possible.</p>
    <p>After swimming in chlorinated water or sea water, undo the braid and rinse immediately under the shower. This is very important to rinse out all of the</p>
  </section>
</main>
</body>
</html>
```